Lumora Signal Website

Looking for a website design that clearly and powerfully portrays our unique and effective indoor advertising billboards in our network.

Our Classic Billboards and Wall Boards are strategically placed in high traffic areas of restaurants, pubs, nightclubs, fitness clubs, colleges & universities, and sports facilities.

Lumora Signal Group is our new name. Our current site is www.brevanopromo.ca
with our focus being entirely on our Out-of-Home Media Networks.

New website address will be www.lumorasignal.ca

We need the following sections:
HOME

PRODUCTS (Drop down menu)
-Classic Billboards
-Wall Boards

NETWORKS (Drop down menu)
-Resto-Bar
-Sports
-Campus
-Casino

FEATURES

CAMPAIGNS

BECOME A PARTNER

CONTACT

Please include social media functions on the homepage such as twitter/facebook/linkdin

We will be supplying content and photos as required.

Our plan is to have you submit the homepage design to start with, and then we can start judging which styles we like the best and can start narrowing our list.

As a second round, we would like to ask the "finalists" to submit a second page (another section of the website) and to see how consistent you are in terms of the look and feel you proposed for the homepage.

Attached is our new logo.

Target Market(s)

Small Business Owners, Advertising Agencies, Media Buyers, Marketing Managers

Industry/Entity Type

Media

Number of Pages Required

1 page

Font styles to use
Sans Serif

Requirements
Must have
• Our Unique Network offers advertising solutions that feature:
• Guaranteed Readership,100% Gender Specific, Frequency, and Captive Audience. Purchasing advertising space in our network are small to medium business owners and advertising agencies booking on behalf of their clients.
• Site must be professional and modern looking.

```html
<!DOCTYPE html>
<html lang="en">
<head>
<meta charset="utf-8">
<title>Lumora Signal Group</title>
<link rel="stylesheet" href="https://fonts.googleapis.com/css2?family=Open+Sans:wght@400;600;700&display=swap">
<style>
:root{
  --red:#b50000;
  --ink:#3a3a3a;
  --body:#555;
  --grey-band:#808080;
  --grey-btn:#7c7c7c;
  --white:#fff;
}
*{box-sizing:border-box;margin:0;padding:0}
html,body{width:918px;height:1200px;overflow:hidden;background:var(--white)}
body{font-family:"Open Sans",Arial,sans-serif;color:var(--body);position:relative}
.site-header{position:absolute;left:0;top:0;width:918px;height:74px}
.brand{position:absolute;left:57px;top:33px;display:flex;align-items:center;gap:6px}
.brand-dot{width:18px;height:18px;border-radius:50%;background:var(--red)}
.brand-name{font-size:21px;font-weight:600;color:var(--red);letter-spacing:-.2px}
.main-nav{position:absolute;left:293px;top:42px;display:flex;gap:0}
.main-nav a{font-size:10px;font-weight:700;color:#333;text-decoration:none;letter-spacing:.3px;padding:0 12.5px;position:relative;height:24px}
.main-nav a.active{color:var(--red)}
.main-nav a.active::after{content:"";position:absolute;left:0;right:0;top:17px;height:5px;background:var(--red)}
.hero{position:absolute;left:0;top:74px;width:918px;height:421px;background:linear-gradient(100deg,#b9b3a6 0%,#c9c2b2 30%,#9d2a2a 45%,#d8d2c6 55%,#6f5a4a 70%,#a9a39a 100%)}
.hero-caption{position:absolute;left:57px;top:150px;width:428px;height:121px;background:rgba(255,255,255,.82);padding:12px 16px}
.hero-caption h1{font-size:27px;font-weight:700;color:var(--red);letter-spacing:.5px;line-height:1.1}
.hero-caption p{font-size:15.5px;color:#222;line-height:20.5px;margin-top:6px;letter-spacing:.3px}
.slider-dots{position:absolute;left:57px;top:383px;display:flex;gap:4px}
.slider-dots span{width:10px;height:10px;border-radius:50%;background:#111}
.slider-dots span.on{background:var(--red)}
.features{position:absolute;left:0;top:530px;width:918px;text-align:center}
.features h2{font-size:15.5px;font-weight:700;color:var(--red);letter-spacing:.4px}
.features p{font-size:13px;line-height:20px;color:#555;width:800px;margin:7px auto 0;letter-spacing:.2px}
.welcome{position:absolute;left:0;top:621px;width:918px;height:226px;background:var(--grey-band);text-align:center;color:var(--white)}
.welcome h2{font-size:21px;font-weight:700;letter-spacing:.8px;margin-top:39px}
.welcome p{font-size:11.3px;line-height:20px;width:800px;margin:13px auto 0}
.btn{display:inline-block;font-size:11px;font-weight:700;color:var(--white);text-decoration:none;letter-spacing:.4px;text-align:center;line-height:31px;height:31px}
.btn-red{background:var(--red);width:98px;margin-top:23px}
.btn-grey{background:var(--grey-btn);width:98px;position:absolute;left:0;top:121px}
.products{position:absolute;left:0;top:872px;width:918px}
.products h2{text-align:center;font-size:21px;font-weight:700;color:#444;letter-spacing:.8px}
.product{position:absolute;top:62px;width:400px;height:153px}
.product-photo{position:absolute;left:0;top:0;width:166px;height:152px}
.product-body{position:absolute;left:186px;top:0;width:200px;height:153px}
.product-body h3{font-size:12px;font-weight:700;color:var(--red);letter-spacing:.3px;margin-top:-2px}
.product-body p{font-size:11.3px;line-height:17.6px;color:#666;margin-top:6px}
.site-footer{position:absolute;left:0;top:1125px;width:918px;height:75px;background:var(--red)}
.site-footer p{position:absolute;left:57px;top:28px;font-size:11.5px;color:var(--white)}
.social{position:absolute;left:762px;top:28px;display:flex;gap:10px}
.social span{width:17px;height:17px;border-radius:3px;background:var(--white)}
</style>
</head>
<body>
<header class="site-header">
  <div class="brand"><span class="brand-dot"></span><span class="brand-name">Lumora Signal Group</span></div>
  <nav class="main-nav">
    <a class="active" href="#">HOME</a>
    <a href="#">PRODUCTS</a>
    <a href="#">NETWORKS</a>
    <a href="#">FEATURES</a>
    <a href="#">CAMPAIGNS</a>
    <a href="#">BECOME A PARTNER</a>
    <a href="#">CONTACT</a>
  </nav>
</header>

<section class="hero" role="img" aria-label="Street scene with red heart-pattern billboards and a woman holding a red heart in a poster frame">
  <div class="hero-caption">
    <h1>LUMORA SIGNAL GROUP</h1>
    <p>Lumora Signal Group is a Canadian out-of-home media company based in Kamloops, British Columbia</p>
  </div>
  <div class="slider-dots"><span class="on"></span><span></span><span></span><span></span></div>
</section>

<section class="features">
  <h2>OUR UNIQUE NETWORK OFFERS ADVERTISING SOLUTIONS THAT FEATURE:</h2>
  <p>Guaranteed Readership,100% Gender Specific, Frequency, and Captive Audience. Purchasing advertising space in our network are small to medium business owners and advertising agencies booking on behalf of their clients.</p>
</section>

<section class="welcome">
  <h2>WELCOME TO OUR WEBSITE</h2>
  <p>Established in 1996, Lumora Signal Group is a Canadian out-of-home media company based in Kamloops, British Columbia.<br>Lumora Signal Group offers innovative and effective indoor Classic Billboards and Wallboards that are strategically placed in high traffic areas of restaurants, pubs, nightclubs, fitness clubs, colleges and universities, and sports arenas.</p>
  <a class="btn btn-red" href="#">READ MORE</a>
</section>

<section class="products">
  <h2>OUR PRODUCTS</h2>
  <article class="product" style="left:57px">
    <div class="product-photo" role="img" aria-label="Framed poster mounted on a tiled restroom wall" style="background:linear-gradient(180deg,#e6e6e6,#cfcfcf)"></div>
    <div class="product-body">
      <h3>CLASSIC BILLBOARD</h3>
      <p>13" x 17" frames are strategically placed inside high traffic restrooms. Reaching consumers in a captive environment.</p>
      <a class="btn btn-grey" href="#">READ MORE</a>
    </div>
  </article>
  <article class="product" style="left:470px">
    <div class="product-photo" role="img" aria-label="Large wall-mounted advertising board on a facility wall" style="background:linear-gradient(180deg,#ecebe7 0%,#ecebe7 22%,#2c2a72 30%,#2c2a72 70%,#ecebe7 78%)"></div>
    <div class="product-body">
      <h3>WALLBOARD</h3>
      <p>48" x 96" billboards are strategically placed on facility walls.</p>
      <a class="btn btn-grey" href="#">READ MORE</a>
    </div>
  </article>
</section>

<footer class="site-footer">
  <p>Copyright © 2016 Lumora Signal Group. All rights reserved.</p>
  <div class="social">
    <span aria-label="Social link"></span><span aria-label="Social link"></span><span aria-label="Social link"></span><span aria-label="Social link"></span>
  </div>
</footer>
</body>
</html>
```